Manufacturers Catalog Cover Page

We are looking to have a cover to our catalog page designed. I currently have begun work for the remained of the catalog in InDesign and want the cover created in InDesign. I will provide photos.

Looking to beable to add the cover to our existing attached catalog.

Industry/Entity Type

Manufacturing

Requirements
Must have
• Colors match what we are currently using. The Dark grey and gold
Nice to have
• modern, clean

```html
<!DOCTYPE html>
<html lang="en">
<head>
<meta charset="utf-8">
<title>Catalog Cover – Rubber &amp; Plastic Extrusion</title>
<link rel="stylesheet" href="https://fonts.googleapis.com/css2?family=Oswald:wght@400;500;600&display=swap">
<style>
  :root {
    --charcoal: #262626;
    --charcoal-light: #333333;
    --stripe: rgba(255,255,255,0.03);
    --gold: #d9a63a;
    --white: #f4f4f4;
    --ink: #2a2a2a;
  }
  * { margin: 0; padding: 0; box-sizing: border-box; }
  html, body { width: 896px; height: 1200px; overflow: hidden; background: var(--charcoal); }
  .cover {
    position: relative; width: 896px; height: 1200px; overflow: hidden;
    background:
      repeating-linear-gradient(135deg, var(--stripe) 0 2px, transparent 2px 14px),
      linear-gradient(180deg, var(--charcoal-light), var(--charcoal));
    font-family: "Oswald", "Arial Narrow", sans-serif;
  }
  .photo-grid { position: absolute; inset: 0; }
  .headline {
    position: absolute; left: 58px; top: 858px; text-transform: uppercase; line-height: 1.04;
  }
  .headline .lead { color: var(--white); font-size: 50px; font-weight: 500; letter-spacing: 1px; display: block; }
  .headline .product { color: var(--gold); font-size: 74px; font-weight: 600; letter-spacing: 1px; display: block; }
  .brand {
    position: absolute; left: 596px; top: 1005px; display: flex; align-items: center; gap: 18px;
  }
  .brand-dot { width: 86px; height: 86px; border-radius: 50%; background: var(--gold); flex: none; }
  .brand-name {
    color: var(--white); font-size: 30px; font-weight: 500; line-height: 1.15; text-transform: uppercase; letter-spacing: 1px;
  }
  .contact-band {
    position: absolute; left: 40px; right: 40px; top: 1130px; height: 46px;
    background: var(--gold); color: var(--ink);
    display: flex; align-items: center; justify-content: center; gap: 18px;
    font-size: 19px; font-weight: 500; letter-spacing: 1px; text-transform: uppercase;
  }
  .contact-band .sep { opacity: 0.7; }
</style>
</head>
<body>
<main class="cover">
  <svg class="photo-grid" width="896" height="1200" viewBox="0 0 896 1200">
    <defs>
      <linearGradient id="g-coach" x1="0" y1="0" x2="0" y2="1">
        <stop offset="0" stop-color="#b88563"/><stop offset="0.55" stop-color="#8c8a86"/><stop offset="1" stop-color="#4a4a4a"/>
      </linearGradient>
      <linearGradient id="g-boat" x1="0" y1="0" x2="1" y2="1">
        <stop offset="0" stop-color="#6fb6d8"/><stop offset="1" stop-color="#1d5f86"/>
      </linearGradient>
      <linearGradient id="g-car" x1="0" y1="0" x2="1" y2="1">
        <stop offset="0" stop-color="#9fc7e2"/><stop offset="1" stop-color="#c9c9c9"/>
      </linearGradient>
      <linearGradient id="g-machine" x1="0" y1="0" x2="1" y2="1">
        <stop offset="0" stop-color="#d9d9d9"/><stop offset="1" stop-color="#e2b52a"/>
      </linearGradient>
      <linearGradient id="g-harvest" x1="0" y1="0" x2="0" y2="1">
        <stop offset="0" stop-color="#7fb3de"/><stop offset="1" stop-color="#d8b03a"/>
      </linearGradient>
      <linearGradient id="g-dig" x1="0" y1="0" x2="0" y2="1">
        <stop offset="0" stop-color="#6aa7de"/><stop offset="0.6" stop-color="#d99a2b"/><stop offset="1" stop-color="#8d6b45"/>
      </linearGradient>
    </defs>

    <polygon class="hero-photo" role="img" aria-label="Photo of a touring motor coach on a desert highway with red rock cliffs"
      points="150,0 896,0 896,470 620,470 150,0" fill="url(#g-coach)"/>

    <polygon class="tile-outline" points="120,160 290,330 120,500 -50,330" fill="none" stroke="var(--gold)" stroke-width="3" opacity="0.5"/>
    <polygon class="tile-outline" points="600,640 770,810 600,980 430,810" fill="none" stroke="var(--gold)" stroke-width="3" opacity="0.5"/>

    <polygon class="tile-photo" role="img" aria-label="Photo of a speedboat on open water"
      points="120,190 260,330 120,470 -20,330" fill="url(#g-boat)"/>

    <polygon class="tile-photo" role="img" aria-label="Photo of a silver sedan on the road"
      points="280,350 420,490 280,630 140,490" fill="url(#g-car)"/>

    <polygon class="tile-photo" role="img" aria-label="Photo of yellow industrial machinery on a factory floor"
      points="440,510 580,650 440,790 300,650" fill="url(#g-machine)"/>

    <polygon class="tile-photo" role="img" aria-label="Photo of a combine harvester in a field"
      points="760,510 900,650 760,790 620,650" fill="url(#g-harvest)"/>

    <polygon class="tile-photo" role="img" aria-label="Photo of a backhoe loader at a construction site"
      points="600,670 740,810 600,950 460,810" fill="url(#g-dig)"/>

    <polygon class="accent" points="40,590 80,630 40,670" fill="var(--gold)" opacity="0.6"/>
  </svg>

  <h1 class="headline">
    <span class="lead">Rubber &amp;</span>
    <span class="lead">Plastic Extusion</span>
    <span class="product">Gaskets</span>
    <span class="product">Trims &amp; Seals</span>
  </h1>

  <div class="brand">
    <span class="brand-dot"></span>
    <span class="brand-name">Resilient<br>Polymers</span>
  </div>

  <footer class="contact-band">
    <span>888-555-0142, 330-555-0187</span>
    <span class="sep">|</span>
    <span>www.resilientpolymers.com</span>
  </footer>
</main>
</body>
</html>
```